Business Card Design

i need a business card to promote my Handyman & Gardening business. It would be nice to see a design incorporating both of these things. We are happy to help in any way we can with no job ever being to small.

Industry/Entity Type

Business

Contact Information for Business Card

Dave's Handyman & Gardening Service
Dave Holt
PO Box 312 Clare SA 5453
dave.holt@fernmail.com
ph 0412 736 508

```html
<!DOCTYPE html>
<html lang="en">
<head>
<meta charset="utf-8">
<title>Dave's Handyman &amp; Gardening Service — Business Card</title>
<link rel="stylesheet" href="https://fonts.googleapis.com/css2?family=Arimo:wght@400&family=Roboto+Condensed:wght@400&display=swap">
<style>
  :root {
    --backdrop: #a3a3a3;
    --card-grey: #c8c8c8;
    --accent-orange: #f26722;
    --stripe-orange: #f4a27a;
    --ink: #111111;
    --white: #ffffff;
  }
  * { margin: 0; padding: 0; box-sizing: border-box; }
  html, body {
    width: 1200px;
    height: 900px;
    overflow: hidden;
    background: var(--backdrop);
  }
  .canvas {
    position: relative;
    width: 1200px;
    height: 900px;
  }
  .business-card {
    position: absolute;
    left: 160px;
    top: 176px;
    width: 880px;
    height: 548px;
    border-radius: 24px;
    background: var(--card-grey);
    overflow: hidden;
    box-shadow: 2px 4px 6px rgba(0, 0, 0, 0.35);
  }
  .name-tab {
    position: absolute;
    left: 0;
    top: 44px;
    height: 56px;
    padding: 0 26px 0 22px;
    background: var(--white);
    border-radius: 0 28px 28px 0;
    display: flex;
    align-items: center;
    gap: 8px;
    font-family: "Arimo", Arial, sans-serif;
    font-size: 24px;
    letter-spacing: 0.5px;
  }
  .name-tab .first-name { color: var(--ink); }
  .name-tab .surname { color: var(--accent-orange); }

  .brand-mark {
    position: absolute;
    left: 290px;
    top: 196px;
    display: flex;
    align-items: center;
    gap: 12px;
  }
  .brand-name {
    font-family: "Roboto Condensed", "Arial Narrow", sans-serif;
    font-size: 32px;
    color: var(--accent-orange);
  }
  .brand-dot {
    width: 26px;
    height: 26px;
    border-radius: 50%;
    background: var(--accent-orange);
  }

  .stripe-set {
    position: absolute;
    left: 0;
    right: 0;
    top: 368px;
    height: 14px;
    background: repeating-linear-gradient(
      to bottom,
      var(--stripe-orange) 0 2px,
      transparent 2px 4px
    );
  }
  .contact-band {
    position: absolute;
    left: 0;
    right: 0;
    bottom: 0;
    height: 166px;
    background: var(--accent-orange);
    padding: 22px 0 0 58px;
  }
  .contact-list { list-style: none; }
  .contact-item {
    display: flex;
    align-items: center;
    gap: 16px;
    height: 40px;
    font-family: "Roboto Condensed", "Arial Narrow", sans-serif;
    font-size: 24px;
    color: var(--ink);
    white-space: nowrap;
  }
  .contact-icon {
    width: 24px;
    height: 24px;
    flex: none;
  }
</style>
</head>
<body>
<main class="canvas">
  <section class="business-card">
    <div class="name-tab">
      <span class="first-name">Name</span>
      <span class="surname">Surname</span>
    </div>

    <div class="brand-mark">
      <span class="brand-name">Dave's Handyman &amp; Gardening</span>
      <span class="brand-dot"></span>
    </div>

    <div class="stripe-set"></div>

    <footer class="contact-band">
      <ul class="contact-list">
        <li class="contact-item">
          <svg class="contact-icon" viewBox="0 0 24 24" aria-hidden="true">
            <path fill="#fff" d="M3 9c0-3 4-5 9-5s9 2 9 5v2h-5V9c-1-.6-2.4-1-4-1s-3 .4-4 1v2H3z"/>
            <path fill="#fff" d="M6 12h12l2 8H4z"/>
            <circle cx="12" cy="16" r="2" fill="#f26722"/>
          </svg>
          <span>0412 736 508</span>
        </li>
        <li class="contact-item">
          <svg class="contact-icon" viewBox="0 0 24 24" aria-hidden="true">
            <rect x="2" y="5" width="20" height="14" fill="#fff"/>
            <path d="M2 5l10 8 10-8M2 19l7-7M22 19l-7-7" fill="none" stroke="#f26722" stroke-width="1.4"/>
          </svg>
          <span>dave.holt@fernmail.com</span>
        </li>
        <li class="contact-item">
          <svg class="contact-icon" viewBox="0 0 24 24" aria-hidden="true">
            <path fill="#fff" d="M12 1a8 8 0 0 0-8 8c0 6 8 14 8 14s8-8 8-14a8 8 0 0 0-8-8z"/>
            <circle cx="12" cy="9" r="3.2" fill="#f26722"/>
          </svg>
          <span>Dave's Handyman &amp; Gardening Service Dave Holt PO Box 312 Wattleby SA 5371</span>
        </li>
      </ul>
    </footer>
  </section>
</main>
</body>
</html>
```